BriarCove Anesthesia Solutions, PC

I need a business card /logo for my new business. I would like it to have some type of ? EKG or medical symbol built into the name( I am on the North side of Lake Pellridge where mountains and water are visible.
I would like this saying on the front," Let our Passion Be your Solution"
My company provides anesthesia services to outparient endoscopy units, eye centers, pain & podiatry offices.

Target Market(s)

Gastroenterologists, podiatrists, eye doctors, pain doctors

Industry/Entity Type

Medical

Contact Information for Business Card

I would like to incorporate a medical symbol(EKG, stethoscope, etc) into the name or scenery if possible

Colors
3377b5
add136
fbee3d

Requirements
Must have
• Business name( BriarCove Anesthesia Solutions,PCI).....
• "Let Our Passion Be your Solution",
• my email: briarcoveanesthesiacare.example,
• 555-214-9087
Nice to have
• Incorporate water &/or mountains

```html
<!DOCTYPE html>
<html lang="en">
<head>
<meta charset="utf-8">
<title>BriarCove Anesthesia Solutions, PC — Business Card</title>
<link rel="stylesheet" href="https://fonts.googleapis.com/css2?family=PT+Sans+Narrow:wght@400;700&display=swap">
<style>
  :root {
    --brand-blue: #3377b5;
    --brand-green: #add136;
    --ink-black: #0b0b0b;
    --paper: #ffffff;
    --backdrop: #5a5a5c;
    --sky-top: #4a4452;
    --sky-glow: #e9927a;
    --water: #8a6a72;
    --shore: #1a1a1c;
  }
  * { box-sizing: border-box; margin: 0; padding: 0; }
  html, body {
    width: 1200px; height: 1000px; overflow: hidden;
    background: var(--backdrop);
    font-family: "PT Sans Narrow", "Arial Narrow", sans-serif;
  }
  .stage {
    width: 1200px; height: 1000px;
    display: flex; flex-direction: column; align-items: center; justify-content: center;
    gap: 56px;
  }
  .card {
    position: relative;
    width: 760px; height: 434px;
    background: var(--paper);
    overflow: hidden;
    box-shadow: 0 10px 24px rgba(0,0,0,.35);
  }
  .card-art { position: absolute; inset: 0; width: 100%; height: 100%; }
  .brand-name {
    position: absolute;
    display: flex; align-items: center; gap: 10px;
    color: var(--brand-green);
    font-weight: 700;
    font-size: 21px;
    line-height: 1.05;
    text-transform: uppercase;
    letter-spacing: .5px;
  }
  .brand-mark {
    width: 26px; height: 26px; flex: none;
    background: var(--brand-green);
  }
  .card-front .brand-name { right: 40px; bottom: 52px; width: 250px; }
  .card-back .brand-name { right: 40px; top: 112px; width: 250px; }
  .tagline {
    position: absolute; left: 70px; top: 42px;
    color: var(--brand-blue);
    font-size: 56px; line-height: 1.02; font-weight: 400;
  }
  .contact {
    position: absolute; left: 60px; bottom: 60px;
    list-style: none;
    color: var(--paper);
    font-size: 26px; line-height: 1.4;
  }
  .contact li { display: flex; align-items: center; gap: 12px; }
  .contact svg { width: 22px; height: 22px; flex: none; }
</style>
</head>
<body>
<main class="stage">

  <section class="card card-front">
    <svg class="card-art" viewBox="0 0 760 434" preserveAspectRatio="none">
      <defs>
        <linearGradient id="lakeTones" x1="0" y1="0" x2="0" y2="1">
          <stop offset="0" stop-color="var(--sky-top)"/>
          <stop offset=".28" stop-color="var(--sky-glow)"/>
          <stop offset=".42" stop-color="var(--shore)"/>
          <stop offset=".5" stop-color="var(--water)"/>
          <stop offset="1" stop-color="#3a3238"/>
        </linearGradient>
      </defs>
      <polygon class="mountain-band" fill="var(--brand-green)"
        points="0,0 760,0 760,232 640,172 600,256 560,214 520,262 470,192 440,284 0,312"/>
      <polygon class="lake-photo" fill="url(#lakeTones)" role="img"
        aria-label="Photograph of a sunset over a lake framed by tree branches"
        points="0,0 760,0 760,206 644,146 598,230 560,188 520,236 470,166 436,262 0,290"/>
    </svg>
    <div class="brand-name"><span class="brand-mark"></span><span>BriarCove Anesthesia Solutions, PC</span></div>
  </section>

  <section class="card card-back">
    <svg class="card-art" viewBox="0 0 760 434" preserveAspectRatio="none">
      <polygon class="accent-band" fill="var(--brand-green)"
        points="0,236 420,300 500,254 540,330 600,262 630,340 760,394 760,434 0,434"/>
      <polygon class="dark-base" fill="var(--ink-black)"
        points="0,262 412,326 494,282 532,358 598,292 622,366 760,424 760,434 0,434"/>
    </svg>
    <p class="tagline">"Let Our Passion<br>&nbsp;Be your Solution"</p>
    <div class="brand-name"><span class="brand-mark"></span><span>BriarCove Anesthesia Solutions, PC</span></div>
    <ul class="contact">
      <li>
        <svg viewBox="0 0 24 24" aria-hidden="true"><path fill="var(--brand-green)" d="M6.6 10.8a15 15 0 0 0 6.6 6.6l2.2-2.2c.3-.3.7-.4 1-.2 1.1.4 2.3.6 3.6.6.6 0 1 .4 1 1V20c0 .6-.4 1-1 1A17 17 0 0 1 3 4c0-.6.4-1 1-1h3.5c.6 0 1 .4 1 1 0 1.3.2 2.5.6 3.6.1.3 0 .7-.2 1z"/></svg>
        <span>555-214-9087</span>
      </li>
      <li>
        <svg viewBox="0 0 24 24" aria-hidden="true"><rect x="2" y="5" width="20" height="14" fill="var(--brand-green)"/><path d="M2 5l10 8 10-8" fill="none" stroke="var(--ink-black)" stroke-width="1.6"/></svg>
        <span>briarcoveanesthesiacare.example</span>
      </li>
    </ul>
  </section>

</main>
</body>
</html>
```